New Business Card Design Project

I would like to purchase a customized version of a design you have previously submitted - https://www.artmarketly.com/design/5184926<br/><br/>I need a design for a swimming pool business card. The services we provide are Maintenance, Repairs and Installations so if you include that in the card. I would also like my email bluecrestpoolsservice@mailora.com, my address 48631 Corvell Dr. Waterford CA, phone number 209-555-0173. Id like to have the two o's in Bluecrest Pools look like an actual pool.

```html
<!DOCTYPE html>
<html lang="en">
<head>
<meta charset="utf-8">
<title>Bluecrest Pool Service – Business Card</title>
<link rel="stylesheet" href="https://fonts.googleapis.com/css2?family=Exo+2:wght@400;500;600&display=swap">
<style>
  :root {
    --backdrop: #d4d4d4;
    --card: #f4f4f4;
    --ink: #231f20;
    --brand-blue: #1d8fe0;
    --wave-fill: #c9e6e1;
    --wave-stripe: #a8d2d2;
    --pin-red: #e0242b;
    --phone-green: #1fa646;
  }
  * { box-sizing: border-box; margin: 0; padding: 0; }
  html, body {
    width: 1200px; height: 1200px; overflow: hidden;
    background: var(--backdrop);
    font-family: "Exo 2", "Segoe UI", sans-serif;
    color: var(--ink);
  }
  .canvas {
    width: 1200px; height: 1200px;
    display: flex; flex-direction: column;
    align-items: center; justify-content: center; gap: 56px;
  }
  .card {
    position: relative;
    width: 900px; height: 514px;
    background: var(--card);
    overflow: hidden;
    box-shadow: 0 6px 18px rgba(0,0,0,0.12);
  }
  .card-wave {
    position: absolute; inset: 0; width: 100%; height: 100%;
  }
  /* Front */
  .card--front { background: #fff; }
  .brand-lockup {
    position: absolute; left: 330px; top: 190px;
    display: flex; align-items: center; gap: 16px;
  }
  .brand-dot {
    width: 34px; height: 34px; border-radius: 50%;
    background: var(--brand-blue);
  }
  .brand-name {
    color: var(--brand-blue); font-weight: 600;
    font-size: 40px; line-height: 1.05;
  }
  /* Back */
  .card-content {
    position: absolute; inset: 0;
    text-align: center;
  }
  .section-title {
    position: absolute; left: 0; right: 0;
    font-weight: 600; font-size: 38px;
  }
  .section-title--services { top: 30px; }
  .section-title--contact { top: 192px; }
  .service-list {
    position: absolute; left: 0; right: 0; top: 98px;
    list-style: none; display: flex; justify-content: center; gap: 22px;
    font-size: 39px; font-weight: 500; padding-left: 18px;
  }
  .service-list li::before { content: "- "; }
  .contact-list {
    position: absolute; left: 145px; top: 240px;
    list-style: none; text-align: left;
    font-size: 39px; line-height: 42px;
  }
  .contact-list li { display: flex; align-items: center; gap: 18px; }
  .contact-icon { width: 36px; height: 36px; flex: none; }
  .footer-name {
    position: absolute; left: 20px; bottom: 26px;
    color: var(--brand-blue); font-weight: 600;
    font-size: 14px; line-height: 1.1; width: 100px; text-align: center;
  }
  .address {
    position: absolute; right: 40px; bottom: 22px;
    display: flex; align-items: center; gap: 6px;
    color: var(--brand-blue); font-size: 31px; font-weight: 500;
  }
  .address svg { width: 18px; height: 30px; }
</style>
</head>
<body>
<main class="canvas">

  <section class="card card--front" aria-label="Card front">
    <svg class="card-wave" viewBox="0 0 985 565" preserveAspectRatio="none" aria-hidden="true">
      <path fill="var(--wave-fill)" d="M0,240 C120,250 260,290 360,360 C450,425 540,500 620,565 L0,565 Z"/>
      <path fill="var(--wave-stripe)" d="M0,225 C150,225 300,270 410,360 C480,420 560,480 640,565 L620,565 C540,490 460,430 390,372 C290,290 150,245 0,240 Z"/>
    </svg>
    <div class="brand-lockup">
      <span class="brand-dot"></span>
      <span class="brand-name">Bluecrest<br>Pool Service</span>
    </div>
  </section>

  <section class="card card--back" aria-label="Card back">
    <svg class="card-wave" viewBox="0 0 985 565" preserveAspectRatio="none" aria-hidden="true">
      <path fill="var(--wave-fill)" d="M0,455 C80,390 180,365 270,372 C450,390 600,478 760,472 C860,468 940,445 985,425 L985,565 L0,565 Z"/>
      <path fill="var(--wave-stripe)" d="M110,388 C250,340 400,378 560,418 C700,452 850,420 985,348 L985,368 C850,442 700,472 560,438 C400,398 250,355 110,388 Z"/>
    </svg>
    <div class="card-content">
      <h2 class="section-title section-title--services">Services :</h2>
      <ul class="service-list">
        <li>Maintenance</li>
        <li>Repairs</li>
        <li>Installations</li>
      </ul>
      <h2 class="section-title section-title--contact">Contact Us :</h2>
      <ul class="contact-list">
        <li>
          <svg class="contact-icon" viewBox="0 0 36 36" aria-hidden="true">
            <rect x="3" y="8" width="30" height="21" rx="2" fill="none" stroke="var(--pin-red)" stroke-width="3"/>
            <path d="M4 10 L18 21 L32 10" fill="none" stroke="var(--pin-red)" stroke-width="3"/>
          </svg>
          bluecrestpoolsservice@mailora.com
        </li>
        <li>
          <svg class="contact-icon" viewBox="0 0 36 36" aria-hidden="true">
            <circle cx="18" cy="18" r="17" fill="var(--phone-green)"/>
            <path fill="#fff" d="M12 9 L15 9 L17 14 L15 16 C16 19 18 21 21 22 L23 20 L28 22 L28 25 C28 27 26 28 24 28 C16 27 10 21 9 13 C9 11 10 9 12 9 Z"/>
          </svg>
          209-555-0173
        </li>
      </ul>
    </div>
    <p class="footer-name">Bluecrest Pool Service</p>
    <p class="address">
      <svg viewBox="0 0 18 30" aria-hidden="true">
        <path fill="var(--pin-red)" d="M9 1 C4 1 1 4.5 1 9 C1 14 9 20 9 29 C9 20 17 14 17 9 C17 4.5 14 1 9 1 Z"/>
        <circle cx="9" cy="9" r="3" fill="#fff"/>
      </svg>
      48631 Corvell Dr. Waterford CA
    </p>
  </section>

</main>
</body>
</html>
```